Meadow Velvet Hair Chalk Package Design

I need a design for my package. I will be selling hair chalk pens. The words Velvet Meadow Hair Chalk must be in there. I want a picture of a unicorn with a lot of hair showing. The hair must contain a mutliple of colors! I want the package to be bright, colorful, sparkly. It can be realistic or cartoonish. Feel free to add additional wording in there that you think might fit. Please see samples so you can get a idea of what I am looking for.

```html
<!DOCTYPE html>
<html lang="en">
<head>
<meta charset="utf-8">
<title>Velvet Meadow Hair Chalk – Package Panels</title>
<link rel="stylesheet" href="https://fonts.googleapis.com/css2?family=Titan+One&family=Nunito:wght@400;700;800&display=swap">
<style>
  :root {
    --bg: #eef0f3;
    --panel: #ffffff;
    --title-red: #e4202a;
    --ink: #1d1d1f;
    --body-ink: #444448;
    --tag-red: #e4202a;
    --tag-pink: #e6177d;
    --tag-green: #3bb54a;
    --tag-blue: #1e88e5;
    --hair-pink: #f0609e;
    --hair-yellow: #f6d43a;
    --hair-orange: #f27a2a;
    --hair-teal: #3fc1c9;
    --hair-purple: #9b59d0;
    --shadow: rgba(30, 30, 40, 0.12);
  }
  * { box-sizing: border-box; margin: 0; padding: 0; }
  html, body { width: 1200px; height: 1200px; overflow: hidden; }
  body {
    background: var(--bg);
    font-family: "Nunito", sans-serif;
    color: var(--ink);
  }
  .canvas {
    position: relative;
    width: 1200px;
    height: 1200px;
    display: flex;
    align-items: center;
    justify-content: center;
    gap: 22px;
  }
  .panel {
    position: relative;
    height: 660px;
    background: var(--panel);
    box-shadow: 0 6px 24px var(--shadow);
    overflow: hidden;
  }
  .panel--back { width: 440px; padding: 34px 30px; }
  .panel--spine { width: 104px; }
  .panel--front { width: 440px; }

  .product-name {
    font-family: "Titan One", sans-serif;
    font-weight: 400;
    color: var(--title-red);
    text-align: center;
    line-height: 1.05;
  }
  .product-name .name-line { display: block; font-size: 26px; letter-spacing: 0.5px; }
  .product-name .name-main { display: block; font-size: 42px; letter-spacing: 1px; }

  .taglines { font-size: 15px; font-weight: 700; line-height: 1.3; }
  .taglines .en { color: var(--tag-red); }
  .taglines .fr { color: var(--tag-pink); }
  .taglines .es { color: var(--tag-green); }

  /* back panel */
  .panel--back .taglines { text-align: center; margin-top: 12px; }
  .back-art {
    position: relative;
    height: 200px;
    margin-top: 18px;
  }
  .ornament-area {
    position: absolute; left: 0; top: 30px;
    width: 130px; height: 110px;
    border-radius: 50%;
    background: radial-gradient(circle, #f8b4c8 0%, #f6d9a8 45%, #cbe9f5 75%, transparent 76%);
  }
  .pens-area {
    position: absolute; right: 0; top: 0;
    width: 240px; height: 200px;
    border-radius: 10px;
    background: linear-gradient(160deg, #8e44c8 0%, #2fa8e0 30%, #2fb84a 52%, #f26b1d 74%, #e83aa0 100%);
    opacity: 0.9;
  }
  .back-lower {
    display: flex;
    gap: 16px;
    margin-top: 18px;
    align-items: flex-end;
  }
  .photo-area {
    flex: 0 0 190px;
    height: 230px;
    border-radius: 6px;
    background: linear-gradient(160deg, #f7e46b 0%, #f58bb8 40%, #d49ad8 70%, #b9e3f2 100%);
  }
  .care-text {
    flex: 1;
    font-size: 9.5px;
    line-height: 1.35;
    color: var(--body-ink);
    text-align: justify;
  }
  .care-text p + p { margin-top: 12px; }

  /* spine */
  .spine-hair {
    height: 200px;
    background: linear-gradient(180deg, var(--hair-pink) 0%, var(--hair-yellow) 30%, var(--hair-teal) 55%, var(--hair-orange) 80%, var(--hair-purple) 100%);
  }
  .spine-name {
    position: absolute;
    left: 50%; top: 430px;
    transform: translate(-50%, -50%) rotate(-90deg);
    white-space: nowrap;
    font-family: "Titan One", sans-serif;
    color: var(--title-red);
    font-size: 24px;
  }

  /* front panel */
  .front-hair {
    position: absolute; left: 0; top: 0;
    width: 100%; height: 240px;
    background: linear-gradient(100deg, var(--hair-yellow) 0%, var(--hair-pink) 20%, var(--hair-orange) 38%, var(--hair-teal) 55%, var(--hair-yellow) 72%, var(--hair-pink) 88%, var(--hair-orange) 100%);
  }
  .front-title {
    position: absolute; left: 50%; top: 22px;
    transform: translateX(-50%);
    background: rgba(255, 255, 255, 0.88);
    border-radius: 12px;
    padding: 6px 16px 8px;
    white-space: nowrap;
  }
  .front-title .name-line { font-size: 22px; }
  .front-title .name-main { font-size: 36px; }
  .pen-window {
    position: absolute; left: 42px; top: 118px;
    width: 356px; height: 100px;
    border-radius: 8px;
    background: linear-gradient(90deg, #f28c5a 0 16.6%, #d9e83a 16.6% 33.3%, #a65fe0 33.3% 50%, #3d5fe8 50% 66.6%, #35c9c0 66.6% 83.3%, #3cc96a 83.3% 100%);
    border: 3px solid rgba(255,255,255,0.7);
  }
  .unicorn-area {
    position: absolute; right: 20px; top: 262px;
    width: 250px; height: 260px;
    border-radius: 46% 54% 40% 60%;
    background: linear-gradient(145deg, #fbfbfb 0%, #f3a6c6 40%, #f6c945 60%, #44b6e0 80%, #9a5cd0 100%);
    opacity: 0.85;
  }
  .contents {
    position: absolute; left: 22px; top: 340px;
    font-size: 13px; font-weight: 800; line-height: 1.35;
  }
  .contents .contents-head { text-decoration: underline; }
  .panel--front .taglines {
    position: absolute; left: 22px; top: 540px;
    font-size: 15px;
  }
  .panel--front .taglines .en { color: var(--tag-blue); }
  .front-footer {
    position: absolute; left: 22px; right: 22px; bottom: 20px;
    display: flex; align-items: flex-end; justify-content: space-between;
  }
  .count { font-size: 16px; font-weight: 800; color: var(--title-red); }
  .net-weight { font-size: 12px; font-weight: 800; }
  .age {
    font-family: "Titan One", sans-serif;
    font-size: 34px; color: var(--title-red); line-height: 1;
  }
</style>
</head>
<body>
<main class="canvas">

  <section class="panel panel--back" aria-label="Back panel">
    <h2 class="product-name">
      <span class="name-line">Velvet Meadow</span>
      <span class="name-main">HAIR CHALK</span>
    </h2>
    <div class="taglines">
      <p class="en">Add temporary streaks color!</p>
      <p class="fr">Ajoute des meches de couleur temporaires!</p>
      <p class="es">Janade mechas de color temporales!</p>
    </div>
    <div class="back-art">
      <div class="ornament-area" role="img" aria-label="Colorful swirl ornament with snowflakes"></div>
      <div class="pens-area" role="img" aria-label="Five hair chalk pens in purple, blue, green, orange and pink"></div>
    </div>
    <div class="back-lower">
      <div class="photo-area" role="img" aria-label="Photo of a girl with rainbow chalked hair in a bun"></div>
      <div class="care-text">
        <p>CAUTION: For external use only. Avoid contact with eyes. WARNING: Small parts, adult supervision advised. ATTENTION: Test on a small strand first. Washes out with regular shampoo. PRECAUCIÓN: Solo para uso externo. Professional grade ingredients. Brush through dry hair, then style as desired. Rinse out with warm water and shampoo.</p>
        <p>Made with care for colorful play days.</p>
      </div>
    </div>
  </section>

  <section class="panel panel--spine" aria-label="Side panel">
    <div class="spine-hair" role="img" aria-label="Rainbow colored hair strands"></div>
    <p class="spine-name">Velvet Meadow HAIR CHALK</p>
  </section>

  <section class="panel panel--front" aria-label="Front panel">
    <div class="front-hair" role="img" aria-label="Photo of wavy rainbow chalked hair"></div>
    <h1 class="product-name front-title">
      <span class="name-line">Velvet Meadow</span>
      <span class="name-main">HAIR CHALK</span>
    </h1>
    <div class="pen-window" role="img" aria-label="Window showing six hair chalk pens in orange, yellow, purple, blue, teal and green"></div>
    <div class="unicorn-area" role="img" aria-label="Illustration of a unicorn with a long multicolored mane"></div>
    <div class="contents">
      <p class="contents-head">CONTAINS:</p>
      <p>.5 Washable Hair</p>
      <p>Chalk Pens</p>
      <p>(0.2oz/6g×5)</p>
      <p>.24 Hair Elastics</p>
      <p>.Easy Instructions</p>
    </div>
    <div class="taglines">
      <p class="en">Add temporary streaks color!</p>
      <p class="fr">Ajoute des meches de couleur temporaires!</p>
      <p class="es">Janade mechas de color temporales!</p>
    </div>
    <div class="front-footer">
      <span class="count">6 Pics</span>
      <span class="net-weight">NET WT/POIDS NET 0.2 (6g)x5</span>
      <span class="age">8+</span>
    </div>
  </section>

</main>
</body>
</html>
```